Laundry pickup and delivery flyer "Fold Harbor laundry"

I need a flyer "8.5"x11" that tells customers about our pickup and delivery laundry service. our website address is: www.foldharborlaundry.example The flyer should be front and back.

Font styles to use
Sans Serif

Colors
0094D4
00A9DD
6FCCEA
C7EBF8
E9F6FB

```html
<!DOCTYPE html>
<html lang="en">
<head>
<meta charset="UTF-8">
<title>Fold Harbor Laundry – Pickup &amp; Delivery Flyer</title>
<link href="https://fonts.googleapis.com/css2?family=Open+Sans:wght@400;600;700;800&display=swap" rel="stylesheet">
<style>
  :root{
    --blue-deep:#2567b3;
    --blue:#0094D4;
    --blue-bright:#00A9DD;
    --blue-soft:#6FCCEA;
    --blue-pale:#C7EBF8;
    --blue-mist:#E9F6FB;
    --ink:#2b2b2b;
    --stage:#8a8a8a;
    --white:#ffffff;
  }
  *{box-sizing:border-box;margin:0;padding:0}
  html,body{width:1200px;height:784px;overflow:hidden}
  body{background:var(--stage);font-family:"Open Sans",Arial,sans-serif;position:relative}
  .page{position:absolute;top:81px;width:481px;height:622px;background:var(--white);overflow:hidden}
  .page--front{left:103px}
  .page--back{left:616px;background:linear-gradient(180deg,var(--white) 0%,var(--blue-mist) 100%)}
  .abs{position:absolute;white-space:nowrap}

  .clouds{position:absolute;left:0;bottom:0;width:481px;height:110px}

  .brand{display:flex;align-items:center;gap:8px;color:var(--blue-deep);font-weight:800;letter-spacing:.5px}
  .brand__dot{width:14px;height:14px;border-radius:50%;background:var(--blue-bright)}
  .front-brand{left:27px;top:50px;font-size:24px}
  .back-brand{left:0;width:481px;top:62px;justify-content:center;font-size:30px}

  .headline{left:27px;top:118px;font-size:26px;line-height:32px;font-weight:800;color:var(--blue-deep)}
  .tagline{left:29px;top:152px;font-size:16px;line-height:25px;color:var(--blue-bright);font-weight:400}

  .photo-clothes{left:21px;top:221px;width:204px;height:166px;background:linear-gradient(160deg,#d9cfe4 0%,#e8d9c8 40%,#e96d5b 70%,#9aaed1 100%);border-radius:4px}
  .photo-ring{left:228px;top:70px;width:262px;height:262px;border-radius:50%;border:14px solid var(--blue);background:linear-gradient(135deg,#d4dde3 0%,#c3ccd3 50%,#b9a88e 100%)}

  .services{left:24px;top:416px;width:202px}
  .services__item{font-size:20.5px;font-weight:800;line-height:24px;color:var(--blue-deep)}
  .services__item--alt{color:var(--blue)}
  .services__rule{height:2px;background:var(--blue-deep);margin:5px 0 6px}

  .why{left:260px;top:340px;font-size:19px;line-height:26px;font-weight:800;color:var(--blue-deep)}
  .perks{left:260px;top:378px;width:208px;list-style:none;white-space:normal}
  .perks li{position:relative;padding-left:20px;font-size:8.4px;line-height:10px;color:var(--ink);margin-bottom:9px}
  .perks li::before{content:"";position:absolute;left:0;top:1px;width:8px;height:8px;border-radius:50%;background:var(--blue-bright)}
  .perks li::after{content:"";position:absolute;left:2.3px;top:2.6px;width:3px;height:1.8px;border-left:1.2px solid var(--white);border-bottom:1.2px solid var(--white);transform:rotate(-45deg)}
  .slogan{left:258px;top:487px;font-size:14px;line-height:17px;font-weight:700;color:var(--blue-bright)}

  .call{left:24px;top:562px;font-size:14px;font-weight:700;color:var(--blue-bright)}
  .phone{left:24px;top:579px;display:flex;align-items:center;gap:6px;font-size:25px;font-weight:800;color:var(--blue-deep)}
  .web{left:288px;top:594px;display:flex;align-items:center;gap:5px;font-size:11px;color:var(--blue)}

  .intro-title{left:0;width:481px;top:140px;text-align:center;font-size:23px;font-weight:800;color:var(--blue-deep)}
  .intro-text{left:30px;width:421px;top:176px;text-align:center;font-size:11.1px;line-height:13.2px;color:var(--ink);white-space:normal}

  .steps{left:23px;top:280px;width:435px;height:122px;border:1.5px solid var(--blue);border-radius:12px}
  .steps__title{left:164px;top:268px;width:152px;height:26px;border-radius:13px;background:var(--blue);color:var(--white);font-size:16.5px;font-weight:700;text-align:center;line-height:26px}
  .step{top:305px;width:100px;text-align:center;font-size:6.8px;line-height:8px;color:#555;white-space:normal}
  .step b{color:var(--blue);font-weight:700}
  .step__icon{width:30px;height:30px;border-radius:50%;background:var(--blue-soft);border:2px solid var(--blue-bright);margin:0 auto 12px;display:flex;align-items:center;justify-content:center}
  .cta{left:60px;top:382px;width:361px;height:35px;border-radius:18px;background:linear-gradient(90deg,var(--blue-deep),var(--blue-bright));color:var(--white);font-size:22.5px;font-weight:800;text-align:center;line-height:35px;letter-spacing:.3px}
  .photo-van{left:60px;top:433px;width:372px;height:112px;border-radius:14px 40px 10px 10px;background:linear-gradient(90deg,#2f7fc4 0%,#2f7fc4 35%,#f2f5f8 45%,#f2f5f8 70%,#3c83c8 100%)}
</style>
</head>
<body>

<section class="page page--front">
  <svg class="clouds" viewBox="0 0 481 110" aria-hidden="true">
    <path d="M0 30 Q20 5 45 25 Q60 45 80 35 Q100 20 130 38 Q160 50 190 40 Q215 30 240 42 Q270 55 300 35 Q320 5 350 10 Q380 15 395 35 Q420 10 450 15 Q470 20 481 5 L481 110 L0 110Z" fill="var(--blue-mist)"/>
    <path d="M140 110 Q150 70 190 75 Q220 60 250 78 Q280 40 320 45 Q360 48 380 70 Q410 55 440 65 Q470 50 481 45 L481 110Z" fill="var(--blue-pale)"/>
  </svg>

  <div class="abs brand front-brand"><span class="brand__dot"></span>Fold Harbor</div>
  <h1 class="abs headline">FOLD HARBOR</h1>
  <p class="abs tagline">HARBORVIEW'S PREMIER<br>LAUNDRY SERVICE</p>

  <div class="abs photo-clothes" role="img" aria-label="Photo of neatly folded stacks of clothes and towels"></div>
  <div class="abs photo-ring" role="img" aria-label="Photo of a customer carrying a laundry basket in a laundromat, framed by a blue ring"></div>

  <div class="abs services">
    <div class="services__item">COMMERCIAL<br>LAUNDRY SERVICE</div>
    <div class="services__rule"></div>
    <div class="services__item services__item--alt">RESIDENTIAL<br>DELIVERY SERVICE</div>
  </div>

  <h2 class="abs why">WHY FOLD HARBOR?</h2>
  <ul class="abs perks">
    <li>Our laundry professionals separate lights and darks to keep your clothes looking great!</li>
    <li>Your items will never be washed with anyone else's</li>
    <li>We use high quality detergents and eco friends chemicals</li>
    <li>No more Laundry day!</li>
  </ul>
  <p class="abs slogan">Outsource laundry. Spend time<br>on what's most important!</p>

  <div class="abs call">Call us Today</div>
  <div class="abs phone">
    <svg width="16" height="16" viewBox="0 0 24 24" aria-hidden="true"><path d="M6.6 10.8a15 15 0 0 0 6.6 6.6l2.2-2.2a1 1 0 0 1 1-.25 11.4 11.4 0 0 0 3.6.57 1 1 0 0 1 1 1V20a1 1 0 0 1-1 1A17 17 0 0 1 3 4a1 1 0 0 1 1-1h3.5a1 1 0 0 1 1 1c0 1.250.2 2.450.57 3.57a1 1 0 0 1-.25 1z" fill="var(--blue-deep)"/></svg>
    555-014-0718
  </div>
  <div class="abs web">
    <svg width="12" height="12" viewBox="0 0 24 24" aria-hidden="true"><circle cx="12" cy="12" r="10" fill="none" stroke="var(--blue)" stroke-width="2"/><path d="M2 12h20M12 2c3 3 3 17 0 20M12 2c-3 3-3 17 0 20" fill="none" stroke="var(--blue)" stroke-width="1.5"/></svg>
    www.foldharborlaundry.example
  </div>
</section>

<section class="page page--back">
  <svg class="clouds" viewBox="0 0 481 110" aria-hidden="true">
    <path d="M0 40 Q25 15 50 35 Q70 60 110 55 Q150 50 200 60 Q260 65 320 60 Q380 55 420 40 Q450 20 481 15 L481 110 L0 110Z" fill="var(--blue-pale)" opacity=".7"/>
  </svg>

  <div class="abs brand back-brand"><span class="brand__dot"></span>Fold Harbor</div>
  <h2 class="abs intro-title">Clean Clothes in a Few Clicks</h2>
  <p class="abs intro-text">Fold Harbor - Harborview, Maine's most advanced and professional laundry service - takes the work out of laundry day with our instant pickup and delivery system. With just a few clicks you can sign up for service and schedule a pickup and delivery time that fits your busy schedule. Your clothes are expertly cleaned to your specifications, folded, packaged, and delivered back to you for easy storage.</p>

  <div class="abs steps"></div>
  <div class="abs steps__title">How It Works</div>

  <div class="abs step" style="left:20px">
    <div class="step__icon"><svg width="16" height="16" viewBox="0 0 24 24" aria-hidden="true"><circle cx="12" cy="12" r="9" fill="none" stroke="#fff" stroke-width="2"/><path d="M12 7v5l3 2" fill="none" stroke="#fff" stroke-width="2"/></svg></div>
    <b>Schedule a pickup here -</b><br>feel free to leave your bag where our driver can get to it.
  </div>
  <div class="abs step" style="left:137px">
    <div class="step__icon"><svg width="16" height="16" viewBox="0 0 24 24" aria-hidden="true"><path d="M2 7h12v9H2zM14 10h4l4 3v3h-8z" fill="none" stroke="#fff" stroke-width="1.8"/><circle cx="6" cy="17" r="2" fill="#fff"/><circle cx="17" cy="17" r="2" fill="#fff"/></svg></div>
    <b>Our driver will pickup</b><br>your clothes at the scheduled time.
  </div>
  <div class="abs step" style="left:244px">
    <div class="step__icon"><svg width="16" height="16" viewBox="0 0 24 24" aria-hidden="true"><rect x="4" y="3" width="16" height="18" rx="2" fill="none" stroke="#fff" stroke-width="1.8"/><circle cx="12" cy="13" r="4" fill="none" stroke="#fff" stroke-width="1.8"/></svg></div>
    <b>Your clothes are expertly</b><br>cleaned by our team of laundry professionals
  </div>
  <div class="abs step" style="left:352px">
    <div class="step__icon"><svg width="16" height="16" viewBox="0 0 24 24" aria-hidden="true"><path d="M8 4l4 3 4-3 5 4-3 3v9H6v-9L3 8z" fill="none" stroke="#fff" stroke-width="1.8"/></svg></div>
    <b>We delivery your clean</b><br>clothes back to you at your convenience!
  </div>

  <div class="abs cta">FREE PICKUP AND DELIVERY</div>
  <div class="abs photo-van" role="img" aria-label="Photo of a branded blue and white delivery van"></div>

  <div class="abs call">Call us Today</div>
  <div class="abs phone">
    <svg width="16" height="16" viewBox="0 0 24 24" aria-hidden="true"><path d="M6.6 10.8a15 15 0 0 0 6.6 6.6l2.2-2.2a1 1 0 0 1 1-.25 11.4 11.4 0 0 0 3.6.57 1 1 0 0 1 1 1V20a1 1 0 0 1-1 1A17 17 0 0 1 3 4a1 1 0 0 1 1-1h3.5a1 1 0 0 1 1 1c0 1.250.2 2.450.57 3.57a1 1 0 0 1-.25 1z" fill="var(--blue-deep)"/></svg>
    555-014-0718
  </div>
  <div class="abs web">
    <svg width="12" height="12" viewBox="0 0 24 24" aria-hidden="true"><circle cx="12" cy="12" r="10" fill="none" stroke="var(--blue)" stroke-width="2"/><path d="M2 12h20M12 2c3 3 3 17 0 20M12 2c-3 3-3 17 0 20" fill="none" stroke="var(--blue)" stroke-width="1.5"/></svg>
    www.foldharborlaundry.example
  </div>
</section>

</body>
</html>
```